Brenmoss Building Company needs a flyer to catch attention

A flyer that can be displayed at several different stores detailing our skills, work produced, experience and contact details. Information can be extracted from our website www.brenmossbc.co.nz. The flyer should feel very green, with addition of pics of work completed as well as stock images of lush green plants, lawns, landscape or similar. Needs to be eye catching with just enough information to express our experience and commitment to high standards

Target Market(s)

Residential
Landscape Architects

Industry/Entity Type

Landscaping

Font styles to use
Serif

Colors
abd037

Requirements
Must have
• Our logo
Experience
Services offered including pictures
All information avail on our website www.brenmossbc.co.nz
Nice to have
• stock images of lush greenery like a garden after fresh rainfall
Should not have
• Nothing comes to mind

```html
<!DOCTYPE html>
<html lang="en">
<head>
<meta charset="utf-8">
<title>Brenmoss Building Company – Flyer</title>
<link rel="stylesheet" href="https://fonts.googleapis.com/css2?family=Fredoka:wght@600;700&family=Tinos:wght@400;700&display=swap">
<style>
  :root {
    --bg: #2b2b2b;
    --green-deep: #0c5a12;
    --green-main: #1b8a1f;
    --green-bright: #2fa52c;
    --lime: #8cc63f;
    --lime-brand: #abd037;
    --pill-dark: #0d4f14;
    --white: #ffffff;
    --logo-text: #1a7a22;
  }
  html, body {
    margin: 0;
    width: 1200px;
    height: 1200px;
    overflow: hidden;
    background: var(--bg);
  }
  .flyer {
    position: absolute;
    left: 190px;
    top: 20px;
    width: 820px;
    height: 1160px;
    overflow: hidden;
    background: var(--green-main);
    font-family: "Tinos", "Times New Roman", serif;
    color: var(--white);
  }
  .hero-photo {
    position: absolute;
    left: 0; top: 0;
    width: 820px; height: 560px;
    background: linear-gradient(160deg, #6f8a4a 0%, #b7a58e 22%, #c9c4bb 45%, #a0533a 62%, #d8d3cb 78%, #8b8a86 100%);
  }
  .green-body {
    position: absolute;
    left: 0; top: 0;
    width: 820px; height: 1160px;
  }
  .brand-badge {
    position: absolute;
    left: 548px; top: 62px;
    width: 236px; height: 236px;
    border-radius: 50%;
    background: var(--white);
    border: 20px solid var(--lime);
    box-sizing: content-box;
    display: flex;
    align-items: center;
    justify-content: center;
    text-align: center;
  }
  .brand-name {
    font-family: "Tinos", "Times New Roman", serif;
    font-weight: 700;
    font-size: 30px;
    line-height: 1.12;
    color: var(--logo-text);
    width: 190px;
  }
  .contact-label {
    position: absolute;
    left: 40px; top: 438px;
    width: 420px; height: 78px;
    border-radius: 14px;
    background: var(--lime);
    display: flex;
    align-items: center;
    gap: 16px;
    padding-left: 22px;
    box-sizing: border-box;
    font-family: "Fredoka", "Arial Rounded MT Bold", sans-serif;
    font-weight: 700;
    font-size: 44px;
  }
  .phone-icon {
    width: 50px; height: 50px;
  }
  .contact-phone {
    position: absolute;
    left: 88px; top: 522px;
    width: 380px; height: 76px;
    border-radius: 14px;
    background: var(--pill-dark);
    display: flex;
    align-items: center;
    justify-content: center;
    font-family: "Fredoka", "Arial Rounded MT Bold", sans-serif;
    font-weight: 700;
    font-size: 48px;
    letter-spacing: 1px;
  }
  .intro {
    position: absolute;
    left: 60px; top: 618px;
    width: 700px;
    margin: 0;
    font-size: 17px;
    line-height: 22px;
    text-align: justify;
  }
  .work-photo {
    position: absolute;
    width: 200px; height: 200px;
    border-radius: 50%;
    border: 14px solid var(--lime);
  }
  .work-photo--deck {
    left: 40px; top: 770px;
    background: linear-gradient(135deg, #4f8cc9 0%, #d9c7a0 35%, #8b4a2b 70%, #5a2e1b 100%);
  }
  .work-photo--path {
    left: 296px; top: 752px;
    background: linear-gradient(135deg, #6ea0d8 0%, #b9b9b4 40%, #8d8d88 70%, #c7c46a 100%);
  }
  .work-photo--terrace {
    left: 552px; top: 734px;
    background: linear-gradient(135deg, #7a8a6a 0%, #3d6b35 35%, #2f3a4a 65%, #9aa0a8 100%);
  }
  .services {
    position: absolute;
    left: 0; top: 990px;
    width: 820px;
    text-align: center;
  }
  .services-title {
    margin: 0 0 6px;
    font-weight: 700;
    font-size: 24px;
    letter-spacing: 1px;
  }
  .services-list {
    margin: 0;
    font-weight: 700;
    font-size: 21px;
    line-height: 27px;
  }
  .sep {
    color: var(--lime);
    font-weight: 400;
    padding: 0 4px;
  }
  .email {
    margin: 10px 0 0;
    font-size: 21px;
  }
</style>
</head>
<body>
  <main class="flyer">
    <div class="hero-photo" role="img" aria-label="Photo of a paved garden terrace with sun loungers, timber pergola and large feature boulders"></div>

    <svg class="green-body" viewBox="0 0 820 1160" aria-hidden="true">
      <defs>
        <linearGradient id="bodyFill" x1="0" y1="0" x2="1" y2="1">
          <stop offset="0" stop-color="#2fa52c"/>
          <stop offset="0.55" stop-color="#1b8a1f"/>
          <stop offset="1" stop-color="#0c5a12"/>
        </linearGradient>
        <linearGradient id="bandFill" x1="0" y1="0" x2="0" y2="1">
          <stop offset="0" stop-color="#116a17"/>
          <stop offset="1" stop-color="#0a4f10"/>
        </linearGradient>
      </defs>
      <path d="M0,600 C200,600 420,560 520,430 C600,320 640,120 760,60 C790,45 810,40 820,40 L820,1160 L0,1160 Z" fill="url(#bodyFill)"/>
      <path d="M0,600 C200,600 420,560 520,430 C600,320 640,120 760,60 C790,45 810,40 820,40" fill="none" stroke="#8cc63f" stroke-width="10"/>
      <path d="M0,1010 L820,930 L820,1160 L0,1160 Z" fill="url(#bandFill)" opacity="0.85"/>
    </svg>

    <div class="brand-badge">
      <span class="brand-name">Brenmoss Building Company</span>
    </div>

    <div class="contact-label">
      <svg class="phone-icon" viewBox="0 0 50 50" aria-hidden="true">
        <circle cx="25" cy="25" r="22" fill="none" stroke="#ffffff" stroke-width="4"/>
        <path d="M17 14 l5 -1 l3 7 l-3 3 c2 4 4 6 8 8 l3 -3 l7 3 l-1 5 c-10 1 -23 -12 -22 -22 z" fill="#ffffff"/>
      </svg>
      <span>Contact Us</span>
    </div>
    <div class="contact-phone">021 555 0148</div>

    <p class="intro">With more than 25 years experience in the landscaping industry, Brenmoss Building Company offers services to large or small residential and commercial projects. Based in Canterbury, we are locally owned and operated. Whether you have a blank canvas or are looking to rejuvenate your property we are able to advise and make the process easy and stress free. From paving, pergolas and decks to concrete or planting your dream garden we have the expertise to help.</p>

    <div class="work-photo work-photo--deck" role="img" aria-label="Photo of a timber deck with slatted screen"></div>
    <div class="work-photo work-photo--path" role="img" aria-label="Photo of a freshly laid paved footpath"></div>
    <div class="work-photo work-photo--terrace" role="img" aria-label="Photo of a tiled courtyard with planted borders"></div>

    <section class="services">
      <h2 class="services-title">OFFERED SERVICES</h2>
      <p class="services-list">
        Patios<span class="sep">|</span>Paving<span class="sep">|</span>Concrete<span class="sep">|</span>Water Features<span class="sep">|</span>Decking<span class="sep">|</span>Fencing<br>
        Boardwalks<span class="sep">|</span>Timber<span class="sep">|</span>Planter Boxes<span class="sep">|</span>Pergolas<span class="sep">|</span>Retaining Walls<br>
        Gardens &amp; Lawns<span class="sep">|</span>Irrigation<span class="sep">|</span>Project Management<span class="sep">|</span>Consultation
      </p>
      <p class="email">Email: info@brenmossbc.co.nz</p>
    </section>
  </main>
</body>
</html>
```